Business Card

We need a business card for a fundraising/sales and marketing company called Kelvora Appeals services. The logo colours are Red Black and white. The final design should communicate professional, reliable yet fun and charity minded
Updates

Sorry for the delay. A decision will be made in the next 48 hours. we are stuck between two designs. Kind Regards, Molly Ravenscroft

Industry/Entity Type

Marketing

```html
<!DOCTYPE html>
<html lang="en">
<head>
<meta charset="utf-8">
<title>Kelvora Appeals services – Business Card</title>
<link rel="stylesheet" href="https://fonts.googleapis.com/css2?family=Montserrat:wght@400;500&family=Old+Standard+TT:ital@1&display=swap">
<style>
  :root {
    --paper: #ffffff;
    --brand-red: #c41511;
    --charcoal: #252a2b;
    --ink-dark: #3b4142;
  }
  html, body {
    margin: 0;
    padding: 0;
    width: 1200px;
    height: 741px;
    overflow: hidden;
    background: var(--paper);
  }
  .card {
    position: relative;
    width: 1200px;
    height: 741px;
    background: var(--paper);
  }
  .card-art {
    position: absolute;
    inset: 0;
  }
  .brand-name {
    position: absolute;
    left: 49px;
    top: 170px;
    margin: 0;
    font-family: "Montserrat", sans-serif;
    font-size: 40px;
    font-weight: 500;
    letter-spacing: 0.3px;
    line-height: 1;
    color: var(--ink-dark);
  }
  .band-name {
    position: absolute;
    right: 42px;
    top: 516px;
    margin: 0;
    font-family: "Montserrat", sans-serif;
    font-weight: 400;
    font-size: 32px;
    line-height: 40px;
    color: var(--paper);
    letter-spacing: 0.3px;
  }
  .contact {
    position: absolute;
    left: 40px;
    top: 606px;
    margin: 0;
    font-family: "Old Standard TT", Georgia, serif;
    font-style: italic;
    font-size: 25.5px;
    line-height: 31px;
    color: var(--paper);
    white-space: nowrap;
  }
  .contact .sep { padding: 0 6px; }
</style>
</head>
<body>
<main class="card">
  <svg class="card-art" width="1200" height="741" viewBox="0 0 1200 741" aria-hidden="true">
    <rect class="card-face" x="17" y="15" width="1167" height="708" fill="var(--brand-red)"/>
    <path class="white-swoop" fill="var(--paper)"
      d="M17 15 L590 15 C598 120 560 210 450 260 C340 310 270 340 257 409
         C240 340 190 300 120 270 C70 248 35 230 17 218 Z"/>
    <rect class="name-band" x="17" y="499" width="1167" height="71" fill="var(--charcoal)"/>
    <circle class="band-emblem" cx="168" cy="528" r="82" fill="var(--charcoal)" stroke="var(--brand-red)" stroke-width="12"/>
  </svg>

  <p class="brand-name">KELVORA APPEALS</p>

  <p class="band-name">KELVORA APPEALS</p>

  <p class="contact">1850 Marlow Ave, Suite 310 Arbordale VA 22419<span class="sep">|</span>Phone : 800-555-0147<span class="sep">|</span>Fax : 703-555-0192<br>Email : sales@kelvoraappeals.com</p>
</main>
</body>
</html>
```